Brightmoor Business Solutions

I need a business card design with logo for my business and management consultancy business. I am based in Singapore and I provide (i) accounting / bookkeeping services; (ii) management and business consultancy solutions; (iii) tax advisory and consultancy; and (iv) risk management and corporate governance. I want the design to be bold and outstanding yet doesn't give the impression that I take unnecessary risks.

Reason: To the designers who have gotten messages from me, I'm still waiting for some changes to be made.

Target Market(s)

Small to large enterprises which are willing to pay value for money and not necessarily the cheapest

Industry/Entity Type

Accounting

Contact Information for Business Card

Name, email address and mobile no.

Requirements
Must have
• If possible, could you incorporate the Sigma symbol as the E for Brightmoor or the Equals sign to show that the business relates to finance / financials and that I provide solutions which may it easy for my clients.
Should not have
• Black / dark backgrounds

```html
<!DOCTYPE html>
<html lang="en">
<head>
<meta charset="utf-8">
<title>Brightmoor Business Solutions – Business Card</title>
<link rel="stylesheet" href="https://fonts.googleapis.com/css2?family=Tinos:wght@400;700&display=swap">
<style>
  :root {
    --canvas-bg: #ecebea;
    --card-white: #ffffff;
    --brand-red: #d3191f;
    --ink: #1a1a1a;
    --faint-grey: #eeeeee;
    --edge-dark: #151515;
  }
  * { box-sizing: border-box; margin: 0; padding: 0; }
  html, body {
    width: 1200px;
    height: 800px;
    overflow: hidden;
    background: var(--canvas-bg);
  }
  .canvas {
    width: 1200px;
    height: 800px;
    display: flex;
    align-items: center;
    justify-content: center;
  }
  .business-card {
    position: relative;
    width: 1000px;
    height: 572px;
    background: var(--card-white);
    overflow: hidden;
    box-shadow: 0 10px 30px rgba(0,0,0,0.15);
    font-family: "Tinos", "Times New Roman", serif;
  }
  .faint-mark {
    position: absolute;
    right: 40px;
    top: 70px;
    width: 300px;
    height: 300px;
    border-radius: 50%;
    background: var(--faint-grey);
  }
  .brand {
    position: absolute;
    left: 70px;
    top: 80px;
    display: flex;
    align-items: center;
    gap: 28px;
  }
  .brand-dot {
    width: 120px;
    height: 120px;
    border-radius: 50%;
    background: var(--brand-red);
    flex: none;
  }
  .brand-name {
    color: var(--brand-red);
    font-weight: 700;
    font-size: 50px;
    line-height: 1.05;
  }
  .contact-block {
    position: absolute;
    left: 70px;
    top: 300px;
  }
  .person-name {
    color: var(--brand-red);
    font-size: 34px;
    font-weight: 400;
    line-height: 1.1;
  }
  .person-role {
    color: var(--ink);
    font-size: 20px;
    margin-bottom: 18px;
  }
  .contact-list { list-style: none; }
  .contact-item {
    display: flex;
    align-items: center;
    gap: 12px;
    color: var(--ink);
    font-size: 28px;
    line-height: 1.35;
  }
  .contact-icon {
    width: 24px;
    height: 24px;
    flex: none;
    fill: var(--brand-red);
  }
  .bottom-rule {
    position: absolute;
    left: 0;
    right: 0;
    bottom: 14px;
    height: 6px;
    background: var(--brand-red);
  }
  .bottom-edge {
    position: absolute;
    left: 0;
    right: 0;
    bottom: 0;
    height: 14px;
    background: var(--card-white);
  }
</style>
</head>
<body>
<main class="canvas">
  <article class="business-card">
    <div class="faint-mark" aria-hidden="true"></div>

    <header class="brand">
      <span class="brand-dot" aria-hidden="true"></span>
      <h1 class="brand-name">Brightmoor<br>Business Solutions</h1>
    </header>

    <section class="contact-block">
      <h2 class="person-name">Mara Quinlan</h2>
      <p class="person-role">Manager</p>
      <ul class="contact-list">
        <li class="contact-item">
          <svg class="contact-icon" viewBox="0 0 24 24" aria-hidden="true"><path d="M6.6 10.8a15.1 15.1 0 0 0 6.6 6.6l2.2-2.2a1 1 0 0 1 1-.25 11.4 11.4 0 0 0 3.6.57 1 1 0 0 1 1 1V20a1 1 0 0 1-1 1A17 17 0 0 1 3 4a1 1 0 0 1 1-1h3.5a1 1 0 0 1 1 1c0 1.25.2 2.45.57 3.57a1 1 0 0 1-.25 1z"/></svg>
          555.214.3096
        </li>
        <li class="contact-item">
          <svg class="contact-icon" viewBox="0 0 24 24" aria-hidden="true"><path d="M12 2a10 10 0 1 0 0 20 10 10 0 0 0 0-20zm6.9 6h-2.9a15.6 15.6 0 0 0-1.4-3.6A8 8 0 0 1 18.9 8zM12 4c.8 1.2 1.5 2.5 1.9 4h-3.8c.4-1.5 1.1-2.8 1.9-4zM4.3 14a8 8 0 0 1 0-4h3.4a16 16 0 0 0 0 4zm.8 2h2.9c.3 1.3.8 2.5 1.4 3.6A8 8 0 0 1 5.1 16zM8 8H5.1a8 8 0 0 1 4.3-3.6C8.8 5.5 8.3 6.7 8 8zm4 12c-.8-1.2-1.5-2.5-1.9-4h3.8c-.4 1.5-1.1 2.8-1.9 4zm2.3-6H9.7a14.7 14.7 0 0 1 0-4h4.6a14.7 14.7 0 0 1 0 4zm.3 5.6c.6-1.1 1.1-2.3 1.4-3.6h2.9a8 8 0 0 1-4.3 3.6zM16.3 14a16 16 0 0 0 0-4h3.4a8 8 0 0 1 0 4z"/></svg>
          www.brightmoor.com
        </li>
        <li class="contact-item">
          <svg class="contact-icon" viewBox="0 0 24 24" aria-hidden="true"><path d="M3 6h18a1 1 0 0 1 1 1v10a1 1 0 0 1-1 1H3a1 1 0 0 1-1-1V7a1 1 0 0 1 1-1zm1 2.2V16h16V8.2l-8 5.3z"/></svg>
          info@brightmoor.com
        </li>
        <li class="contact-item">
          <svg class="contact-icon" viewBox="0 0 24 24" aria-hidden="true"><path d="M12 3 2 12h3v8h5v-5h4v5h5v-8h3z"/></svg>
          418 Harbor Lane Eastfield
        </li>
      </ul>
    </section>

    <div class="bottom-rule" aria-hidden="true"></div>
    <div class="bottom-edge" aria-hidden="true"></div>
  </article>
</main>
</body>
</html>
```